Cleaning Company Banner

Looking to have a Banner made that shows our contact information and shows what we do with good imagery to catch cars driving by. Will be a 6' x 3' banner (landscape). Attached our logo and flyer that we currently hand out.

```html
<!DOCTYPE html>
<html lang="en">
<head>
<meta charset="utf-8">
<title>BrightEdge Cleaning Banner</title>
<link href="https://fonts.googleapis.com/css2?family=Montserrat:wght@500;600;700;800&display=swap" rel="stylesheet">
<style>
  :root{
    --sky:#7fd3f5;
    --white:#ffffff;
    --ink:#111418;
    --teal:#1fb9a6;
    --blue:#2f86c9;
    --mid-blue:#2a8bd0;
    --navy:#163f70;
    --deep-navy:#0f2f5a;
  }
  *{margin:0;padding:0;box-sizing:border-box}
  html,body{width:1200px;height:600px;overflow:hidden;background:var(--white)}
  .banner{
    position:relative;width:1200px;height:600px;overflow:hidden;
    background:linear-gradient(180deg,var(--sky) 0%,#d9f2fc 12%,var(--white) 19%,var(--white) 100%);
    font-family:"Montserrat",sans-serif;color:var(--ink);
  }
  .artwork{position:absolute;inset:0;width:1200px;height:600px}
  .brand-name{
    position:absolute;left:60px;width:420px;top:168px;text-align:center;
    font-weight:700;font-size:46px;line-height:1.05;color:var(--blue);letter-spacing:1px;
  }
  .services{
    position:absolute;left:30px;width:480px;top:293px;text-align:center;
    font-weight:500;font-size:30px;line-height:39px;color:var(--ink);
  }
  .call-line{
    position:absolute;left:144px;top:396px;display:flex;align-items:center;gap:15px;
    font-weight:500;font-size:31px;color:var(--ink);
  }
  .call-icon{width:42px;height:42px}
  .phone-number{
    position:absolute;left:42px;top:470px;
    font-weight:800;font-size:80px;letter-spacing:-2px;color:var(--white);line-height:1;
  }
  .contact-row{
    position:absolute;display:flex;align-items:center;gap:22px;
    font-weight:700;font-size:26px;color:var(--white);
  }
  .contact-row.web{left:677px;top:481px}
  .contact-row.mail{left:687px;top:545px}
  .contact-icon{width:34px;height:34px}
</style>
</head>
<body>
<div class="banner">
  <svg class="artwork" viewBox="0 0 1200 600" xmlns="http://www.w3.org/2000/svg">
    <defs>
      <linearGradient id="phoneBand" x1="0" y1="0" x2="1" y2="0.3">
        <stop offset="0" stop-color="#1fb9a6"/>
        <stop offset="0.45" stop-color="#2a8bd0"/>
        <stop offset="1" stop-color="#163f70"/>
      </linearGradient>
      <linearGradient id="webBand" x1="0" y1="0" x2="1" y2="0">
        <stop offset="0" stop-color="#0f2f5a"/>
        <stop offset="0.6" stop-color="#1f5f9e"/>
        <stop offset="1" stop-color="#2a8bd0"/>
      </linearGradient>
      <linearGradient id="mailBand" x1="0" y1="0" x2="1" y2="0">
        <stop offset="0" stop-color="#1fb9a6"/>
        <stop offset="0.35" stop-color="#2a8bd0"/>
        <stop offset="1" stop-color="#0f2f5a"/>
      </linearGradient>
      <linearGradient id="photoDusting" x1="0" y1="0" x2="1" y2="1">
        <stop offset="0" stop-color="#f4f2ee"/>
        <stop offset="0.5" stop-color="#dfe6f0"/>
        <stop offset="1" stop-color="#e9d3bf"/>
      </linearGradient>
      <linearGradient id="photoVacuum" x1="0" y1="0" x2="0" y2="1">
        <stop offset="0" stop-color="#b9ad9c"/>
        <stop offset="0.6" stop-color="#6d665d"/>
        <stop offset="1" stop-color="#c7bba6"/>
      </linearGradient>
      <linearGradient id="photoWipe" x1="0" y1="0" x2="1" y2="1">
        <stop offset="0" stop-color="#e6e9ec"/>
        <stop offset="0.45" stop-color="#9cc6d8"/>
        <stop offset="1" stop-color="#f0cf3a"/>
      </linearGradient>
    </defs>

    <!-- photo panel: dusting -->
    <polygon points="506,95 708,68 690,418 567,415" fill="var(--blue)"/>
    <g role="img" aria-label="Photo of a hand dusting a white door frame with a blue duster">
      <polygon points="531,112 730,86 707,432 582,432" fill="url(#photoDusting)" stroke="var(--blue)" stroke-width="2"/>
    </g>

    <!-- photo panel: vacuum -->
    <polygon points="752,30 880,30 936,358 731,377" fill="var(--teal)"/>
    <g role="img" aria-label="Photo of a vacuum cleaner on a patterned carpet">
      <polygon points="768,47 896,47 950,370 746,392" fill="url(#photoVacuum)" stroke="var(--teal)" stroke-width="2"/>
    </g>

    <!-- photo panel: wiping -->
    <polygon points="925,97 1127,72 1105,420 976,420" fill="var(--blue)"/>
    <g role="img" aria-label="Photo of a yellow gloved hand wiping a surface with a blue cloth">
      <polygon points="948,114 1150,92 1128,438 1000,438" fill="url(#photoWipe)" stroke="var(--blue)" stroke-width="2"/>
    </g>

    <!-- contact bands -->
    <polygon points="0,450 635,450 672,600 0,600" fill="url(#phoneBand)"/>
    <polygon points="640,467 1200,467 1200,533 656,533" fill="url(#webBand)"/>
    <polygon points="656,533 1200,533 1200,600 672,600" fill="url(#mailBand)"/>
  </svg>

  <div class="brand-name">BrightEdge<br>Cleaning</div>

  <p class="services">Residential, Commercial,<br>and Construction Cleaning</p>

  <div class="call-line">
    <svg class="call-icon" viewBox="0 0 42 42" aria-hidden="true">
      <defs>
        <linearGradient id="callFill" x1="0" y1="0" x2="1" y2="1">
          <stop offset="0" stop-color="#2a8bd0"/>
          <stop offset="1" stop-color="#0f2f5a"/>
        </linearGradient>
      </defs>
      <circle cx="21" cy="21" r="21" fill="url(#callFill)"/>
      <path d="M15 12c1-1 2-1 3 0l2 3c.6 1 .3 1.8-.4 2.4l-1 .8c.8 2 2.3 3.6 4.3 4.5l.9-1c.6-.7 1.5-.9 2.4-.3l3 2c1 .8 1 1.8.1 2.8l-1.2 1.3c-1.4 1.3-3.8 1-6.7-1-3-2-5.4-4.8-6.9-7.8-1.2-2.8-1.2-5 .5-6.7z" fill="var(--white)"/>
    </svg>
    <span>Call or Text</span>
  </div>

  <div class="phone-number">(555)014-2938</div>

  <div class="contact-row web">
    <svg class="contact-icon" viewBox="0 0 34 34" aria-hidden="true">
      <circle cx="17" cy="17" r="17" fill="var(--white)"/>
      <circle cx="17" cy="17" r="10" fill="none" stroke="var(--teal)" stroke-width="2"/>
      <ellipse cx="17" cy="17" rx="4.5" ry="10" fill="none" stroke="var(--blue)" stroke-width="1.8"/>
      <line x1="7" y1="17" x2="27" y2="17" stroke="var(--blue)" stroke-width="1.8"/>
    </svg>
    <span>www.brightedgecleaning.com</span>
  </div>

  <div class="contact-row mail">
    <svg class="contact-icon" viewBox="0 0 34 34" aria-hidden="true">
      <circle cx="17" cy="17" r="17" fill="var(--white)"/>
      <rect x="8" y="11" width="18" height="12" rx="1.5" fill="var(--blue)"/>
      <polyline points="8.5,11.5 17,18 25.5,11.5" fill="none" stroke="var(--white)" stroke-width="1.6"/>
    </svg>
    <span>hello@brightedgecleaning.com</span>
  </div>
</div>
</body>
</html>
```